Freelance IT consultant - minimalist website

I am an independent IT consultant / contractor with established clients. In many cases I sub-contract through other IT companies when performing work for external clients, in which case I am obliged to adopt these other companies' corporate branding. However I am becoming aware that my personal inclusion / involvement is adding significant value to these 3rd party companies' offerings, making them more attractive to their clients. I would like to capitalise on that value by developing my own "personal brand" - providing a means of distinguishing myself from other companies through whom I sub-contract. I figure a personal website would be a good place to start!

I want a design which evokes concepts of "smart, sensible solutions"; "clean and concise". My "competitors" have a tendency towards jargon, and verbose, often meaningless prose. I would like to position myself as the "go to man" for the solution - pure and simple - once all of the posturing and postulating has been finished. (NB: I've used the tagline "Solutions - Pure and Simple" for this project, but I'm receptive to other suggestions!)

Finally (...do you believe that? :-) ) my particular forte is Geographic Information Systems (GIS) and spatial databases. So if a website design can somehow incorporate the idea of maps, or the globe, that'd be brilliant (but keep this subtle - I'm not a cartographer and don't wish to convey that suggestion.) Something that suggests the connection between information and databases with maps and locations, perhaps?

Examples / concepts I like:
"Solution" - this is what I do! Often to ill-described, uncertain problems.
http://brovaquest.org/wp-content/uploads/2013/11/Solution.jpg
http://www.quorvelbridge.com.au/Media/Picture/Solutions.jpg

"Elegant design" - this is what I (like to think I) do :-)
http://qmmdelvaro.files.zenblogly.com/2013/03/nautilus1.png
http://static.pexilbox.com/static/61d329ccf5c162d73102b4ec/t/61d357adf5c11c64d75c9899/1465010548160/Nautilus_Shell.png?format=1000w
Updates

I've added a PDF file with some unstructured thoughts and ideas around what I'm after. I realise I've left this brief quite open-ended - I don't mean to make it difficult. I'm really after some graphic design creative brilliance, more than website technical brilliance. Hope this helps!

I've uploaded an excerpt from my personal CV in a bid to answer some of the ... well, quite reasonable questions I'm receiving about what the hell it is that I actually do! By way of explanation, I didn't upload this information - or indeed, by entire CV - originally, because I really am seeking something more timeless than a "latest CV." As I've indicated, I'm really trying to create a web presence to confirm my right to "be here". I fully expect that any serious customers who visit my site will follow through with a "contact me" action, at which time I will be able to respond with a discussion and/or CV tailored to a particular project. That's what I do. As for the not-so-serious visitors to my site, I'd like them to leave with an affirming nod and the mental note that, they've stumbled upon somebody credible. And if they bookmark the site, all the better! :-) Hope this helps!

Reason: I'd really like a couple of extra days to run these ideas past some friends and colleagues. This is great stuff - but like so many deadlines, this one snuck up a bit quicker than I was expecting!

Target Market(s)

Prospective clients already aware of my existence, seeking confirmation / reassurance of my bona-fides and relevance. Typically government or mainstream business IT procurement staff.

Industry/Entity Type

Contractor

Requirements
Must have
• Simple, clean, timeless (?) design. I want a stable, solid web "presence" but don't expect to have to "work" the site at all. It's a brochure, really. But that doesn't mean it can't be a good one!
Nice to have
• Incorporate new logo (currently subject of a separate ArtMarrow project - no: 482917)
Single page design - (I could be persuaded otherwise, but can't see the need for more than one really!)
Should not have
• Rolling banners, smiling actors / actresses, etc (I have no interest in updating these images!)
Shopping cart, news feeds, blah, blah... This is a static advertising presence only.

```html
<!DOCTYPE html>
<html lang="en">
<head>
<meta charset="utf-8">
<title>Kelvard IT – Smart Solutions</title>
<link rel="stylesheet" href="https://fonts.googleapis.com/css2?family=Ubuntu:wght@300;400;500&display=swap">
<style>
:root{
  --brand:#0a72c3;
  --brand-deep:#0866b0;
  --ink:#2e2e2e;
  --text:#555;
  --white:#fff;
  --rule:#0a72c3;
}
*{box-sizing:border-box;margin:0;padding:0}
html,body{width:946px;height:1200px;overflow:hidden;background:var(--white)}
body{position:relative;font-family:"Ubuntu",sans-serif;color:var(--text)}

.hero{position:absolute;left:0;top:0;width:946px;height:741px;overflow:hidden}
.hero-photo{position:absolute;inset:0;
  background:
    radial-gradient(ellipse 260px 200px at 740px 360px,#3b6fb0 0%,rgba(40,70,120,.55) 45%,rgba(0,0,0,0) 100%),
    linear-gradient(90deg,#d9dadb 0%,#c9cacb 40%,#8d8f91 70%,#4a4b4d 100%);}
.hero-photo::after{content:"";position:absolute;left:0;right:0;bottom:0;height:220px;
  background:linear-gradient(180deg,rgba(0,0,0,0),rgba(60,55,50,.45))}

.brand{position:absolute;left:46px;top:0;width:125px;height:114px;background:var(--brand);
  display:flex;align-items:flex-end;padding:0 0 14px 10px}
.brand-name{color:var(--white);font-size:13px;font-weight:500;letter-spacing:1.5px}

.contact-bar{position:absolute;top:23px;right:46px;display:flex;gap:36px;font-size:12px;font-weight:300;color:var(--white)}
.contact-bar span{display:flex;align-items:center;gap:10px}
.contact-bar svg{fill:var(--brand)}

.nav{position:absolute;top:58px;left:593px;display:flex;align-items:center}
.nav a{display:block;height:29px;line-height:29px;padding:0 13px;font-size:11px;color:var(--white);text-decoration:none}
.nav a.active{background:var(--brand)}
.nav .search{margin-left:28px}

.hero-copy{position:absolute;left:46px;top:246px;color:var(--ink)}
.hero-kicker{font-size:35px;font-weight:400;letter-spacing:1px;line-height:1}
.hero-title{font-size:62px;font-weight:500;line-height:1;letter-spacing:1px;margin-top:0}
.hero-lede{margin-top:18px;width:440px;font-size:11px;font-weight:300;line-height:17px;color:#3a3a3a}

.features{position:absolute;left:40px;top:533px;display:flex;gap:3px}
.feature{width:289px;height:139px;background:rgba(8,110,195,.93);display:flex;padding:30px 20px 0 26px;gap:14px;color:var(--white)}
.feature:last-child{width:281px}
.feature svg{flex:none;stroke:var(--white);fill:none;stroke-width:1.6}
.feature h3{font-size:19px;font-weight:400;margin-bottom:8px}
.feature p{font-size:10px;font-weight:300;line-height:15px}

.services{position:absolute;left:0;top:820px;width:946px;text-align:center}
.section-title{font-size:16px;font-weight:400;letter-spacing:4.5px;color:var(--brand);padding-bottom:12px;
  width:138px;margin:0 auto;border-bottom:1px solid var(--rule)}
.section-lede{width:420px;margin:22px auto 0;font-size:11.5px;font-weight:300;line-height:17px}

.service-grid{position:absolute;top:164px;left:36px;display:flex}
.service{width:292px;text-align:center}
.service svg{fill:var(--brand);display:block;margin:0 auto;height:44px}
.service h4{margin-top:20px;font-size:13px;font-weight:400;color:#333}
.service p{margin-top:18px;font-size:11.5px;font-weight:300;line-height:17px}
</style>
</head>
<body>
<header class="hero">
  <div class="hero-photo" role="img" aria-label="Photo of a desk with a laptop showing a puzzle and a monitor reading Solution, Strategy, Consulting, Success"></div>

  <div class="brand"><span class="brand-name">KELVARD IT</span></div>

  <div class="contact-bar">
    <span><svg width="13" height="10" viewBox="0 0 13 10"><path d="M0 0h13v1.5L6.5 5.5 0 1.5zM0 3l6.5 4L13 3v7H0z"/></svg>hello@kelvardit.net</span>
    <span><svg width="11" height="11" viewBox="0 0 11 11"><path d="M2 0l2 3-1.3 1.3a7 7 0 0 0 4 4L8 7l3 2-1.2 1.8C5 11 0 6 .2 1.2z"/></svg>(555) 318-2046</span>
  </div>

  <nav class="nav">
    <a class="active" href="#">HOME</a>
    <a href="#">SERVICES</a>
    <a href="#">ABOUT US</a>
    <a href="#">CONTACT</a>
    <svg class="search" width="12" height="12" viewBox="0 0 12 12" fill="none" stroke="#fff" stroke-width="1.8"><circle cx="5" cy="5" r="3.8"/><path d="M8 8l3 3"/></svg>
  </nav>

  <div class="hero-copy">
    <div class="hero-kicker">SMART SOLUTIONS</div>
    <h1 class="hero-title">IT CONSULTANT</h1>
    <p class="hero-lede">Praesent faucibus nisl sit nulla sollicitudin a sed purus. Lorem Ipsum. Proin gravida nibh vel velit auctor. Aenean sollicitudin, lorem quis bibendum auctor.</p>
  </div>

  <div class="features">
    <div class="feature">
      <svg width="38" height="36" viewBox="0 0 38 36"><path d="M2 2h34v26H14l-8 6v-6H2z"/><text x="17" y="18" font-size="14" fill="#fff" stroke="none" font-family="Ubuntu,sans-serif">?</text></svg>
      <div><h3>Ask Me Anything</h3><p>Praesent faucibus nisl Lorem Ipsum.<br>Proin gravida nibh vel velit auctor<br>aliquet.</p></div>
    </div>
    <div class="feature">
      <svg width="36" height="36" viewBox="0 0 36 36"><circle cx="18" cy="18" r="16"/><ellipse cx="18" cy="18" rx="7" ry="16"/><path d="M2 18h32M5 10h26M5 26h26M18 2v32"/></svg>
      <div><h3>Brand &amp; Identity</h3><p>Praesent faucibus nisl Lorem Ipsum.<br>Proin gravida nibh vel velit auctor<br>aliquet.</p></div>
    </div>
    <div class="feature">
      <svg width="42" height="36" viewBox="0 0 42 36"><circle cx="16" cy="11" r="8"/><path d="M2 34c0-9 6-14 14-14s14 5 14 14z"/><path d="M25 4a8 8 0 0 1 0 15M32 22c5 2 8 6 8 12h-6"/></svg>
      <div><h3>Adding Value</h3><p>Praesent faucibus nisl Lorem Ipsum.<br>Proin gravida nibh vel velit auctor<br>aliquet.</p></div>
    </div>
  </div>
</header>

<section class="services">
  <h2 class="section-title">SERVICES</h2>
  <p class="section-lede">Lorem ipsum dolor sit amet, consectetur adipiscing elit. Maecenas ac augue at erat hendrerit dictum. Praesent porta, purus eget sagittis imperdiet.</p>

  <div class="service-grid">
    <div class="service">
      <svg width="50" height="44" viewBox="0 0 50 36"><path d="M10 36a9 9 0 0 1-1-18 12 12 0 0 1 23-6 8 8 0 0 1 10 7 9 9 0 0 1-2 17z"/></svg>
      <h4>IT Consultant / Contractor</h4>
      <p>Praesent faucibus nisl sit nulla sollicitudin a sed<br>purus augue at erat hendrerit</p>
    </div>
    <div class="service">
      <svg width="28" height="44" viewBox="0 0 28 40"><path d="M14 0a14 14 0 0 0-14 14c0 10 14 26 14 26s14-16 14-26A14 14 0 0 0 14 0zm0 8a6 6 0 1 1 0 12 6 6 0 0 1 0-12z" fill-rule="evenodd"/></svg>
      <h4>Geographic Information Systems</h4>
      <p>voluptatem accusantium.Sed ut perspiciatis unde<br>omnis augue at erat hendrerit</p>
    </div>
    <div class="service">
      <svg width="40" height="44" viewBox="0 0 40 46"><ellipse cx="20" cy="6" rx="20" ry="6"/><path d="M0 10c0 4 9 7 20 7s20-3 20-7v8c0 4-9 7-20 7S0 22 0 18zM0 22c0 4 9 7 20 7s20-3 20-7v8c0 4-9 7-20 7S0 34 0 30zM0 34c0 4 9 7 20 7s20-3 20-7v6c0 4-9 6-20 6S0 44 0 40z"/></svg>
      <h4>Spatial Databases</h4>
      <p>Praesent faucibus nisl sit nulla sollicitudin a sed<br>purus augue at erat hendrerit</p>
    </div>
  </div>
</section>
</body>
</html>
```